- Redesign our business card
- Logo remains unchanged
- Current business card attached

Target Market(s)

We are a property management company

Industry/Entity Type

Business

```html
<!DOCTYPE html>
<html lang="en">
<head>
<meta charset="utf-8">
<title>Harcourt Property Group – Business Card</title>
<link rel="stylesheet" href="https://fonts.googleapis.com/css2?family=Roboto:wght@400;500;700&display=swap">
<style>
  :root {
    --stage: #000000;
    --card: #ffffff;
    --card-shade: #f1f1f0;
    --olive: #7f7c3c;
    --ink: #3f3f3f;
    --grey: #6e6e6e;
    --rule: #9a9a9a;
    --faint: #e7e5dc;
  }
  * { margin: 0; padding: 0; box-sizing: border-box; }
  html, body {
    width: 1200px; height: 900px; overflow: hidden;
    background: var(--stage);
    font-family: "Roboto", Arial, sans-serif;
  }
  .canvas { position: relative; width: 1200px; height: 900px; }
  .card {
    position: absolute; left: 244px; width: 664px; height: 390px;
    border-radius: 22px; overflow: hidden;
    background: linear-gradient(180deg, var(--card) 0%, var(--card) 60%, var(--card-shade) 100%);
  }
  .card--front { top: 36px; }
  .card--back { top: 466px; }
  .watermark-block { position: absolute; background: var(--faint); }
  .card--front .watermark-block { left: 0; top: 0; width: 300px; height: 220px; opacity: .7; }
  .card--back .watermark-block { right: 0; bottom: 0; width: 300px; height: 260px; opacity: .8; }

  .brand { position: absolute; display: flex; align-items: center; gap: 10px; }
  .brand-square { width: 14px; height: 14px; background: var(--olive); flex: none; }
  .brand-name { color: var(--olive); font-weight: 700; letter-spacing: .02em; white-space: nowrap; }
  .tagline { position: absolute; color: var(--grey); letter-spacing: .06em; white-space: nowrap; }

  .card--front .brand { left: 368px; top: 166px; }
  .card--front .brand-name { font-size: 18px; }
  .card--front .tagline { left: 392px; top: 192px; font-size: 13px; }

  .holder { position: absolute; left: 22px; top: 238px; }
  .holder-name { color: var(--olive); font-weight: 700; font-size: 20px; letter-spacing: .03em; }
  .holder-role { color: var(--ink); font-size: 17px; margin-top: 4px; }

  .contact { position: absolute; top: 316px; font-size: 12.5px; line-height: 17px; color: var(--ink); }
  .contact--address { left: 22px; width: 250px; font-weight: 700; text-transform: uppercase; }
  .contact--phone { left: 292px; padding-left: 20px; border-left: 1px solid var(--rule); height: 56px; }
  .contact--web { left: 418px; padding-left: 20px; border-left: 1px solid var(--rule); height: 56px; }

  .card--back .brand { left: 0; right: 0; top: 250px; justify-content: center; }
  .card--back .brand-name { font-size: 30px; letter-spacing: .05em; }
  .card--back .tagline { left: 0; right: 0; top: 292px; text-align: center; font-size: 19px; letter-spacing: .1em; }
  .card--back .site { position: absolute; left: 0; right: 0; top: 342px; text-align: center;
    font-size: 14px; letter-spacing: .3em; color: var(--grey); }
</style>
</head>
<body>
<main class="canvas">
  <section class="card card--front">
    <div class="watermark-block"></div>
    <div class="brand"><span class="brand-square"></span><span class="brand-name">HARCOURT PROPERTY GROUP</span></div>
    <p class="tagline">STRATA MANAGEMENT SERVICES</p>
    <div class="holder">
      <p class="holder-name">DANIEL HARCOURT</p>
      <p class="holder-role">Licensed Strata Manager</p>
    </div>
    <p class="contact contact--address">PO Box 48, Elmwood Vale NSW 2011 12/6-10 Larkin Street Elmwood Vale NSW 2011</p>
    <p class="contact contact--phone">T: 02 9000 0147<br>F: 02 9000 0148<br>M: 0400 000 21</p>
    <p class="contact contact--web">E: info@harcourtproperty.com.au<br>www.harcourtproperty.com.au</p>
  </section>

  <section class="card card--back">
    <div class="watermark-block"></div>
    <div class="brand"><span class="brand-square"></span><span class="brand-name">HARCOURT PROPERTY GROUP</span></div>
    <p class="tagline">STRATA MANAGEMENT SERVICES</p>
    <p class="site">www.harcourtproperty.com.au</p>
  </section>
</main>
</body>
</html>
```